new business card design - modern, professional, bold, B2B focus - with QR code pls

we are looking for a modern looking, colorful, business card design. some highlights:
- put space for QR code please. probably on the back but I'm open.
- biz card to be orientated VERTICAL not the traditional horizontal.
- do NOT use our full name on the card (ie: Allied Furnace Servicing Inc). Use only AFS Inc or AFS.
- use black and orange with some white. ideally black card with orange and white for the letters/logo etc. gray ok too - for outlines etc.
- we work in HEAVY industrial, so the cards should lend itself to this. our website is alfurnace.example, so you can see what we do.
- do NOT put in little smoke stack pictures / silouettes etc.
- think MODERN and INDUSTRIAL, with a techy focus.

Industry/Entity Type

heavy industrial - all of them. we perform maintenance and inspection services at heavy industrial and commercial businesses. so B2B

Contact Information for Business Card

name, title, phone numbers (cell + hardline), website, email address. of course our logo too - either on front or front and back.

Font styles to use
Other font styles liked:
• montserrat

Colors
F0912C
F2A743
F7CA91
FBE8D2
FDF5EE

Requirements
Must have
• see description
Nice to have
• see description
Should not have
• see description

```html
<!DOCTYPE html>
<html lang="en">
<head>
<meta charset="utf-8">
<title>AFS Inc — Business Card Set</title>
<link href="https://fonts.googleapis.com/css2?family=Oswald:wght@600;700&family=Montserrat:wght@300&display=swap" rel="stylesheet">
<style>
  :root {
    --backdrop: #363636;
    --card-black: #000000;
    --card-white: #ffffff;
    --brand-orange: #fcae12;
    --ink: #231f20;
    --dot-tone: #2a2a2a;
  }
  * { margin: 0; padding: 0; box-sizing: border-box; }
  html, body { width: 1200px; height: 1200px; overflow: hidden; background: var(--backdrop); }
  .sheet { position: relative; width: 1200px; height: 1200px; }

  .card { position: absolute; width: 272px; height: 476px; overflow: hidden; }
  .card--back { background: var(--card-black); }
  .card--front { background: var(--card-white); }

  /* Back side */
  .back-url {
    position: absolute; left: 22px; top: 334px;
    transform: rotate(-90deg); transform-origin: left top;
    font-family: "Montserrat", sans-serif; font-weight: 300;
    font-size: 19px; color: var(--card-white); white-space: nowrap; letter-spacing: 0.2px;
  }
  .brand-wordmark {
    position: absolute; left: 52px; top: 200px; width: 200px;
    font-family: "Oswald", sans-serif; font-weight: 700;
    font-size: 134px; line-height: 1; color: var(--brand-orange); letter-spacing: 0;
    white-space: nowrap;
  }
  .dot-field {
    position: absolute; border-radius: 4px;
    background: linear-gradient(135deg, var(--dot-tone), #1a1a1a);
  }
  .card--back .dot-field { left: 35px; top: 366px; width: 134px; height: 84px; }
  .card--front .dot-field { left: 116px; top: 26px; width: 134px; height: 84px;
    background: linear-gradient(135deg, #e4e4e4, #f2f2f2); }

  /* Front side */
  .holder-name {
    position: absolute; left: 30px; top: 142px;
    font-family: "Oswald", sans-serif; font-weight: 700;
    font-size: 34px; line-height: 1; color: var(--ink);
  }
  .holder-title {
    position: absolute; left: 30px; top: 180px;
    font-family: "Oswald", sans-serif; font-weight: 700;
    font-size: 16px; line-height: 1; color: var(--ink);
  }
  .rule-bar { position: absolute; left: 30px; right: 0; top: 210px; height: 14px; background: var(--card-black); }
  .contact-band { position: absolute; left: 0; right: 0; top: 224px; height: 158px; background: var(--brand-orange); }
  .contact-list { position: absolute; left: 27px; top: 42px; list-style: none; }
  .contact-item {
    display: flex; align-items: center; gap: 10px; height: 20px; margin-bottom: 12px;
    font-family: "Oswald", sans-serif; font-weight: 600; font-size: 18px; color: var(--ink);
  }
  .contact-item:nth-child(2) { margin-bottom: 14px; }
  .contact-icon { width: 20px; height: 20px; flex: none; }
  .web-band {
    position: absolute; left: 0; right: 0; top: 382px; height: 68px; background: var(--card-black);
    font-family: "Oswald", sans-serif; font-weight: 700; font-size: 31px; color: var(--card-white);
    padding-left: 30px; line-height: 66px;
  }
  .foot-band { position: absolute; left: 0; right: 0; top: 450px; bottom: 0; background: var(--brand-orange); }
</style>
</head>
<body>
<svg width="0" height="0" style="position:absolute">
  <defs>
    <symbol id="icon-mobile" viewBox="0 0 20 20">
      <rect width="20" height="20" fill="#231f20"/>
      <rect x="6" y="3" width="8" height="14" rx="1" fill="none" stroke="#fff" stroke-width="1.6"/>
      <rect x="9" y="14" width="2" height="1.4" fill="#fff"/>
    </symbol>
    <symbol id="icon-phone" viewBox="0 0 20 20">
      <rect width="20" height="20" fill="#231f20"/>
      <path d="M6 4.5 L8.3 4.5 L9.2 7.6 L7.8 8.8 C8.6 10.6 9.6 11.7 11.2 12.4 L12.4 11 L15.5 11.9 L15.5 14.2 C15.5 15 14.8 15.6 14 15.5 C9 14.8 5.3 11 4.5 6 C4.4 5.2 5.1 4.5 6 4.5 Z" fill="#fff"/>
    </symbol>
    <symbol id="icon-mail" viewBox="0 0 20 20">
      <rect width="20" height="20" fill="#231f20"/>
      <rect x="4" y="6" width="12" height="8.5" fill="#fff"/>
      <path d="M4 6 L10 10.6 L16 6" fill="none" stroke="#231f20" stroke-width="1.3"/>
    </symbol>
  </defs>
</svg>

<main class="sheet">
  <!-- Row 1 -->
  <section class="card card--back" style="left:157px; top:102px;">
    <span class="back-url">alfurnace.example</span>
    <span class="brand-wordmark">AFS</span>
    <div class="dot-field" role="img" aria-label="Grid of white dots"></div>
  </section>

  <section class="card card--front" style="left:466px; top:102px;">
    <div class="dot-field" role="img" aria-label="Grid of black dots"></div>
    <h1 class="holder-name">MARK ELLISON</h1>
    <p class="holder-title">DIRECTOR</p>
    <div class="rule-bar"></div>
    <div class="contact-band">
      <ul class="contact-list">
        <li class="contact-item"><svg class="contact-icon"><use href="#icon-mobile"/></svg>+1 4820 37615</li>
        <li class="contact-item"><svg class="contact-icon"><use href="#icon-phone"/></svg>+1 7391 26084</li>
        <li class="contact-item"><svg class="contact-icon"><use href="#icon-mail"/></svg>contact@alfurnace.example</li>
      </ul>
    </div>
    <div class="web-band">alfurnace.example</div>
    <div class="foot-band"></div>
  </section>

  <section class="card card--back" style="left:770px; top:102px;">
    <span class="back-url">alfurnace.example</span>
    <span class="brand-wordmark">AFS</span>
    <div class="dot-field" role="img" aria-label="Grid of white dots"></div>
  </section>

  <!-- Row 2 -->
  <section class="card card--front" style="left:156px; top:619px;">
    <div class="dot-field" role="img" aria-label="Grid of black dots"></div>
    <h1 class="holder-name">MARK ELLISON</h1>
    <p class="holder-title">DIRECTOR</p>
    <div class="rule-bar"></div>
    <div class="contact-band">
      <ul class="contact-list">
        <li class="contact-item"><svg class="contact-icon"><use href="#icon-mobile"/></svg>+1 4820 37615</li>
        <li class="contact-item"><svg class="contact-icon"><use href="#icon-phone"/></svg>+1 7391 26084</li>
        <li class="contact-item"><svg class="contact-icon"><use href="#icon-mail"/></svg>contact@alfurnace.example</li>
      </ul>
    </div>
    <div class="web-band">alfurnace.example</div>
    <div class="foot-band"></div>
  </section>

  <section class="card card--back" style="left:466px; top:619px;">
    <span class="back-url">alfurnace.example</span>
    <span class="brand-wordmark">AFS</span>
    <div class="dot-field" role="img" aria-label="Grid of white dots"></div>
  </section>

  <section class="card card--front" style="left:770px; top:619px;">
    <div class="dot-field" role="img" aria-label="Grid of black dots"></div>
    <h1 class="holder-name">MARK ELLISON</h1>
    <p class="holder-title">DIRECTOR</p>
    <div class="rule-bar"></div>
    <div class="contact-band">
      <ul class="contact-list">
        <li class="contact-item"><svg class="contact-icon"><use href="#icon-mobile"/></svg>+1 4820 37615</li>
        <li class="contact-item"><svg class="contact-icon"><use href="#icon-phone"/></svg>+1 7391 26084</li>
        <li class="contact-item"><svg class="contact-icon"><use href="#icon-mail"/></svg>contact@alfurnace.example</li>
      </ul>
    </div>
    <div class="web-band">alfurnace.example</div>
    <div class="foot-band"></div>
  </section>
</main>
</body>
</html>
```